Nail Technician Business Card Design

My business is a nail technician business which involves applying nail enhancements to clients nails. I would like a design that uses the colours:, purple or black and silver on a light grey background. The final design should entice clients to my business.
I would like appointment times on the back of the card.
I want the spilled bottle on the front and the other one on the back
I would like the dragonfly font
Updates
Reason: I have found a font I would like used and also an image/logo
I have listed some ideas I would like used on the design of my card. thanks
Petra
Industry/Entity Type
Business
Contact Information for Business Card
Lumira Nail Designs
47 Wexcombe street,
Dunedoo, NSW 2851
Mobile: 0400 582 316
Petra Hawkins
Like us on Glowbook
Font styles to use
Other font styles liked:
- Dragonfly
Look and feel
Each slider illustrates characteristics of the customer's brand and the style your logo design should communicate.

```html
<!DOCTYPE html>
<html lang="en">
<head>
<meta charset="utf-8">
<title>Petra Hawkins Nail Designs – Business Card</title>
<link rel="stylesheet" href="https://fonts.googleapis.com/css2?family=Sofia&display=swap">
<style>
  :root {
    --canvas-bg: #e6e4e8;
    --card-bg: #ffffff;
    --ink-magenta: #b0198f;
    --ink-magenta-soft: #c54ab0;
    --powder-light: #c9a3d8;
    --powder-deep: #7b2f86;
    --skin-light: #f3dccb;
    --skin-mid: #e2b79c;
    --polish-pink: #d0349f;
    --polish-dark: #3a1236;
    --card-shadow: rgba(40, 30, 45, 0.28);
  }
  * { margin: 0; padding: 0; box-sizing: border-box; }
  html, body { width: 1200px; height: 1000px; overflow: hidden; }
  body {
    background: var(--canvas-bg);
    position: relative;
    font-family: "Sofia", cursive;
    color: var(--ink-magenta);
  }
  .card {
    position: absolute;
    width: 525px;
    height: 300px;
    background: var(--card-bg);
    box-shadow: 0 8px 22px var(--card-shadow);
    overflow: hidden;
  }

  /* Back of card */
  .card--back { left: 70px; top: 170px; }
  .back__visual {
    position: absolute;
    left: 18px; top: 40px;
    width: 200px; height: 220px;
    border-radius: 40% 45% 35% 50%;
    background: radial-gradient(ellipse at 55% 50%, var(--powder-deep) 0%, var(--ink-magenta-soft) 35%, var(--powder-light) 65%, rgba(255,255,255,0) 100%);
  }
  .back__details {
    position: absolute;
    left: 225px; top: 26px;
    width: 290px;
    text-align: center;
  }
  .back__address { font-size: 18px; line-height: 1.25; }
  .back__phone { font-size: 26px; line-height: 1.15; }
  .back__social { font-size: 16px; line-height: 1.3; }
  .appointment {
    position: absolute;
    left: 245px; top: 132px;
    width: 260px;
    font-size: 20px;
  }
  .appointment__row { display: flex; align-items: baseline; margin-bottom: 16px; }
  .appointment__line {
    flex: 1;
    margin-left: 6px;
    border-bottom: 2px dotted var(--ink-magenta);
    height: 1px;
  }
  .appointment__row--date .appointment__line { max-width: 110px; }
  .appointment__row--time .appointment__line { max-width: 115px; }

  /* Front of card */
  .card--front { left: 605px; top: 470px; }
  .front__portrait {
    position: absolute;
    left: 0; top: 0;
    width: 300px; height: 300px;
    background:
      linear-gradient(90deg, rgba(255,255,255,0) 70%, #ffffff 100%),
      linear-gradient(160deg, var(--skin-light) 0%, var(--skin-mid) 55%, #ffffff 100%);
  }
  .front__brand {
    position: absolute;
    right: 28px; top: 76px;
    text-align: right;
  }
  .front__name { font-size: 36px; font-weight: 400; line-height: 1; }
  .front__tagline {
    font-size: 20px;
    color: var(--ink-magenta-soft);
    margin-top: 4px;
  }
  .front__spill {
    position: absolute;
    right: 24px; bottom: 24px;
    width: 220px; height: 80px;
    border-radius: 45% 30% 30% 45%;
    background: linear-gradient(100deg, var(--ink-magenta-soft) 0%, var(--polish-pink) 55%, var(--polish-dark) 100%);
  }
</style>
</head>
<body>

  <section class="card card--back" aria-label="Back of business card">
    <div class="back__visual" role="img" aria-label="Purple nail polish bottle on crushed purple powder"></div>
    <div class="back__details">
      <p class="back__address">47 Wexcombe street Merrivale</p>
      <p class="back__phone">0400582316</p>
      <p class="back__social">Like us on Glowbook</p>
    </div>
    <div class="appointment">
      <p class="appointment__row">Your appointment:</p>
      <p class="appointment__row appointment__row--date">Date: <span class="appointment__line"></span></p>
      <p class="appointment__row appointment__row--time">Time: <span class="appointment__line"></span></p>
    </div>
  </section>

  <section class="card card--front" aria-label="Front of business card">
    <div class="front__portrait" role="img" aria-label="Photograph of a woman with manicured magenta nails"></div>
    <div class="front__brand">
      <h1 class="front__name">Petra Hawkins</h1>
      <p class="front__tagline">Nail designs</p>
    </div>
    <div class="front__spill" role="img" aria-label="Spilled pink nail polish bottle"></div>
  </section>

</body>
</html>
```